Flyer Design for Norvane LLC

We need a Flyer for a new company called “Norvane LLC”. This is a technology process improvement company providing a comprehensive assessment of the technology used to run their business. The documentation and review process delivers the visibility and reassurance they need to protect their business and plan for the future. The product is called “Systems Pathcharting”. Our primary target is small-medium size businesses, with the deliverables going to the decision maker.

We would like to see the designs use the color blue. Our tag line is "Protect Your Business · Take Control of IT".

- Attached: Norvane LLC Overview document we put together as a starting point. Use as much or as little as you wish.
- Attached: Business Card and Logo designs for colors, etc.

Industry/Entity Type

It Company

```html
<!DOCTYPE html>
<html lang="en">
<head>
<meta charset="utf-8">
<title>Norvane LLC – Systems Pathcharting Flyer</title>
<link rel="stylesheet" href="https://fonts.googleapis.com/css2?family=Lato:wght@400;700&family=Oswald:wght@400;500;600;700&family=Roboto+Condensed:wght@400;700&display=swap">
<style>
:root{
  --blue:#1a7fd4;
  --blue-deep:#1468b8;
  --ink:#222;
  --charcoal:#3b3b3b;
  --paper:#fff;
  --soft:#f2f2f2;
  --backdrop:#e9e9e9;
}
*{margin:0;padding:0;box-sizing:border-box}
html,body{width:1200px;height:1200px;overflow:hidden;background:var(--backdrop)}
.flyer{position:absolute;left:152px;top:20px;width:895px;height:1160px;background:var(--paper);overflow:hidden;box-shadow:0 2px 10px rgba(0,0,0,.15);font-family:'Lato',sans-serif;color:var(--ink)}
.header{position:absolute;left:0;top:0;width:895px;height:438px}
.header-photo{position:absolute;inset:0;clip-path:polygon(307px 0,895px 0,895px 438px,393px 438px);background:linear-gradient(120deg,#9aa3ad 0%,#c9c4be 35%,#7d858f 60%,#5c636c 100%)}
.header-rule{position:absolute;left:0;top:438px;width:895px;height:6px;background:#bdbdbd}
.brand{position:absolute;left:0;width:330px;top:120px;text-align:center;display:flex;align-items:center;justify-content:center;gap:10px}
.brand-dot{width:26px;height:26px;border-radius:50%;background:var(--blue)}
.brand-name{font-family:'Oswald',sans-serif;font-weight:600;font-size:34px;color:var(--blue);letter-spacing:2px}
.tagline{position:absolute;left:41px;width:284px;top:236px;text-align:center;white-space:nowrap}
.tag-protect{font-family:'Oswald',sans-serif;font-weight:400;font-size:92px;line-height:92px;color:transparent;-webkit-text-stroke:2px var(--ink);letter-spacing:1px}
.tag-business{font-family:'Lato',sans-serif;font-weight:700;font-size:40px;line-height:46px;color:var(--blue);margin-top:4px}
.tag-control{font-family:'Oswald',sans-serif;font-weight:700;font-size:33px;line-height:42px;color:var(--ink);letter-spacing:-0.3px}
.intro{position:absolute;left:0;top:444px;width:895px;height:311px;background:var(--blue);color:#fff;text-align:center}
.intro-title{font-family:'Oswald',sans-serif;font-weight:500;font-size:40px;margin-top:22px;letter-spacing:1px}
.pill{display:inline-block;background:var(--charcoal);color:#fff;font-family:'Roboto Condensed',sans-serif;font-weight:700;font-size:19px;height:32px;line-height:32px;border-radius:16px;padding:0 16px}
.pill.first{width:235px;margin-top:10px}
.pill.second{width:200px;margin-top:8px}
.intro p{font-size:13.5px;line-height:17px;margin:6px auto 0;width:830px}
.intro p.gap{margin-top:17px}
.areas-title{position:absolute;left:33px;top:768px;font-family:'Oswald',sans-serif;font-weight:500;font-size:27px;color:var(--blue)}
.cycle{position:absolute;left:83px;top:778px}
.area-label{position:absolute;font-size:15.5px;line-height:19px;color:var(--ink)}
.divider{position:absolute;left:567px;top:800px;width:1px;height:280px;background:#e2e2e2}
.deliverables{position:absolute;left:581px;top:810px}
.deliverables h3{font-family:'Oswald',sans-serif;font-weight:400;font-size:20px;color:var(--blue);margin-bottom:12px}
.deliverables ul{list-style:none}
.deliverables li{display:flex;align-items:center;gap:11px;font-size:16.5px;height:27px}
.footer{position:absolute;left:0;top:1096px;width:895px;height:58px;background:var(--blue)}
.footer-tab{position:absolute;left:0;top:0;width:225px;height:42px;background:var(--charcoal);clip-path:polygon(0 0,225px 0,190px 42px,0 42px);color:#fff;font-family:'Roboto Condensed',sans-serif;font-size:26px;line-height:42px;padding-left:31px;white-space:nowrap}
.contact{position:absolute;top:12px;display:flex;align-items:center;gap:8px;color:#fff;font-family:'Roboto Condensed',sans-serif;font-size:16px;white-space:nowrap}
</style>
</head>
<body>
<div class="flyer">
  <header class="header">
    <div class="header-photo" role="img" aria-label="Photo of a smiling business team in suits standing in an office corridor"></div>
    <div class="brand"><span class="brand-dot"></span><span class="brand-name">NORVANE LLC</span></div>
    <div class="tagline">
      <div class="tag-protect">PROTECT</div>
      <div class="tag-business">Your Business</div>
      <div class="tag-control">TAKE CONTROL OF IT</div>
    </div>
  </header>
  <div class="header-rule"></div>

  <section class="intro">
    <h1 class="intro-title">SYSTEMS PATHCHARTING</h1>
    <div class="pill first">You have big plans, right?</div>
    <p>Technology may help you get there, but how can you plan where you want to go without defining where you are today?</p>
    <div class="pill second">We can help!</div>
    <p>Norvane LLC provides a comprehensive assessment of the technology used to run your business. The documentation and review process delivers the visibility and reassurance you need to protect your business.</p>
    <p class="gap">Our team understands that each business operates on its own unique complexities, and crafting a solution requires a custom, unbiased review. Positioning your company with the right insight is intrumental to your success and our goal as your technology partner.</p>
  </section>

  <h2 class="areas-title">Evaluating Five Functional Areas</h2>
  <svg class="cycle" width="300" height="300" viewBox="0 0 300 300" aria-hidden="true">
    <g stroke="#555" stroke-width="1">
      <line x1="150" y1="150" x2="150" y2="50"/>
      <line x1="150" y1="150" x2="240" y2="115"/>
      <line x1="150" y1="150" x2="211" y2="230"/>
      <line x1="150" y1="150" x2="90" y2="231"/>
      <line x1="150" y1="150" x2="62" y2="112"/>
    </g>
    <circle cx="150" cy="150" r="100" fill="none" stroke="#3b3b3b" stroke-width="6"/>
    <g fill="#3b3b3b">
      <polygon points="160,40 160,60 178,50"/>
      <polygon points="232,102 252,102 244,122"/>
      <polygon points="224,222 226,244 206,238"/>
      <polygon points="80,222 72,242 94,242"/>
      <polygon points="52,116 70,118 64,96"/>
    </g>
    <g fill="#1a7fd4" stroke="#fff" stroke-width="2">
      <circle cx="95" cy="69" r="19"/>
      <circle cx="206" cy="64" r="19"/>
      <circle cx="245" cy="173" r="19"/>
      <circle cx="150" cy="250" r="19"/>
      <circle cx="54" cy="173" r="19"/>
    </g>
    <g fill="#fff">
      <rect x="90" y="62" width="10" height="14" rx="2"/>
      <rect x="197" y="60" width="18" height="9" rx="1"/>
      <rect x="239" y="166" width="12" height="14" rx="2"/>
      <rect x="143" y="252" width="14" height="4" rx="1"/>
      <rect x="47" y="166" width="13" height="15" rx="1"/>
    </g>
  </svg>
  <div class="area-label" style="left:32px;top:826px;text-align:center;width:110px">IT<br>Administration</div>
  <div class="area-label" style="left:331px;top:818px">IT service<br>Delivery</div>
  <div class="area-label" style="left:367px;top:936px">Infrastructure<br>Services</div>
  <div class="area-label" style="left:185px;top:1051px;width:100px;text-align:center">Application<br>Services</div>
  <div class="area-label" style="left:40px;top:947px;width:70px;text-align:center">IT<br>Planning</div>

  <div class="divider"></div>
  <div class="deliverables">
    <h3>Dossier Deliverables</h3>
    <ul>
      <li><svg width="18" height="18" viewBox="0 0 18 18"><rect x="1" y="3" width="14" height="14" rx="2" fill="none" stroke="#333" stroke-width="1.6"/><path d="M4 9l4 4 9-11" fill="none" stroke="#333" stroke-width="1.8"/></svg>Executive Dashboard</li>
      <li><svg width="18" height="18" viewBox="0 0 18 18"><rect x="1" y="3" width="14" height="14" rx="2" fill="none" stroke="#333" stroke-width="1.6"/><path d="M4 9l4 4 9-11" fill="none" stroke="#333" stroke-width="1.8"/></svg>Technology Product Summary</li>
      <li><svg width="18" height="18" viewBox="0 0 18 18"><rect x="1" y="3" width="14" height="14" rx="2" fill="none" stroke="#333" stroke-width="1.6"/><path d="M4 9l4 4 9-11" fill="none" stroke="#333" stroke-width="1.8"/></svg>Recommended IT Policies</li>
      <li><svg width="18" height="18" viewBox="0 0 18 18"><rect x="1" y="3" width="14" height="14" rx="2" fill="none" stroke="#333" stroke-width="1.6"/><path d="M4 9l4 4 9-11" fill="none" stroke="#333" stroke-width="1.8"/></svg>Potential Cost Savings</li>
      <li><svg width="18" height="18" viewBox="0 0 18 18"><rect x="1" y="3" width="14" height="14" rx="2" fill="none" stroke="#333" stroke-width="1.6"/><path d="M4 9l4 4 9-11" fill="none" stroke="#333" stroke-width="1.8"/></svg>Technology Recommendations</li>
      <li><svg width="18" height="18" viewBox="0 0 18 18"><rect x="1" y="3" width="14" height="14" rx="2" fill="none" stroke="#333" stroke-width="1.6"/><path d="M4 9l4 4 9-11" fill="none" stroke="#333" stroke-width="1.8"/></svg>In-depth Questionnaire</li>
      <li><svg width="18" height="18" viewBox="0 0 18 18"><rect x="1" y="3" width="14" height="14" rx="2" fill="none" stroke="#333" stroke-width="1.6"/><path d="M4 9l4 4 9-11" fill="none" stroke="#333" stroke-width="1.8"/></svg>Technology Product Details</li>
      <li><svg width="18" height="18" viewBox="0 0 18 18"><rect x="1" y="3" width="14" height="14" rx="2" fill="none" stroke="#333" stroke-width="1.6"/><path d="M4 9l4 4 9-11" fill="none" stroke="#333" stroke-width="1.8"/></svg>Full Infrastructure Detailed Report</li>
    </ul>
  </div>

  <footer class="footer">
    <div class="footer-tab">Contact Info :</div>
    <div class="contact" style="left:241px">
      <svg width="26" height="18" viewBox="0 0 26 18"><path d="M2 6c6-6 16-6 22 0l-3 3-4-2V5H9v2L5 9z" fill="#fff"/><rect x="6" y="10" width="14" height="7" rx="2" fill="#fff"/></svg>866-555-0142</div>
    <div class="contact" style="left:440px">
      <svg width="22" height="22" viewBox="0 0 22 22" fill="none" stroke="#fff" stroke-width="1.6"><circle cx="11" cy="11" r="9"/><ellipse cx="11" cy="11" rx="4" ry="9"/><line x1="2" y1="11" x2="20" y2="11"/></svg>www.norvanellc.com</div>
    <div class="contact" style="left:666px">
      <svg width="40" height="18" viewBox="0 0 40 18" fill="none" stroke="#fff" stroke-width="1.6"><line x1="1" y1="5" x2="9" y2="5"/><line x1="3" y1="9" x2="9" y2="9"/><line x1="5" y1="13" x2="9" y2="13"/><rect x="13" y="2" width="25" height="15" rx="2"/><path d="M13 3l12 8 12-8"/></svg>sales@norvanellc.com</div>
  </footer>
</div>
</body>
</html>
```